Marwood Holiday Jubilee 2025

We’re looking for a designer to help refresh the visual identity of our annual Christmas show while maintaining continuity from previous years. The updated design should feel festive, and warm, with a sense of celebration and anticipation. We’d like a central graphic that can be adapted for posters, social media, and digital signage, along with supporting assets for flyers and banners.

We’re open to seasonal color palettes such as rich reds, deep greens or blues, golds, silvers, or cool winter tones, and prefer typography that’s clear and elegant. The overall look should feel familiar to returning audiences while inviting and engaging for newcomers.

Two key groups: the current attenders of our congregation and the broader community in our suburb of Rochester, NY. Our congregation is made up of families, older adults, and young professionals who value faith, community and spiritual growth. The surrounding community is a fast growing friendly and family-oriented area of young professionals and longtime families.

We’re looking for a designer to help refresh the visual identity of our annual Christmas show while maintaining continuity with the theme and tone of previous years. The updated design should feel festive, and warm, with a sense of celebration and anticipation. We’d like a central graphic that can be adapted for posters, social media, and digital signage, along with supporting assets for flyers and banners.

Target Market(s)

Two key groups: the current attenders of our congregation and the broader community in our suburb of Rochester, NY. Our congregation is made up of families, older adults, and young professionals who value faith, community and spiritual growth. The surrounding community is a fast growing friendly and family-oriented area of young professionals and long time families.

Industry/Entity Type

Non-profit. Church

Font styles to use
Serif
Decorative
Script
Other font styles liked:
• Quentin

Requirements
Must have
• Sparkle, eye catching
Should not have
• must not look identical to the uploaded versions

```html
<!DOCTYPE html>
<html lang="en">
<head>
<meta charset="utf-8">
<title>Marwood Holiday Jubilee 2025</title>
<link rel="stylesheet" href="https://fonts.googleapis.com/css2?family=Kaushan+Script&family=Montserrat:ital,wght@0,600;0,700;1,800&family=Questrial&display=swap">
<style>
  :root {
    --page: #ffffff;
    --pine-deep: #123a24;
    --pine-mid: #2f6a3c;
    --pine-light: #5f8f6a;
    --frost: #cfd8dc;
    --bokeh-blue: #3f6fc4;
    --white: #ffffff;
    --lime: #c9e41c;
    --rule-yellow: #e6e84a;
    --rule-pale: #e9e7a8;
    --red: #ff1010;
  }
  * { margin: 0; padding: 0; box-sizing: border-box; }
  html, body {
    width: 1200px; height: 800px; overflow: hidden;
    background: var(--page);
  }
  .canvas { position: relative; width: 1200px; height: 800px; }
  .hero-photo {
    position: absolute; left: 141px; top: 128px; width: 918px; height: 540px;
    background:
      radial-gradient(circle at 88% 8%, var(--frost) 0, rgba(207,216,220,0) 22%),
      radial-gradient(circle at 60% 30%, rgba(63,111,196,.55) 0, rgba(63,111,196,0) 30%),
      radial-gradient(circle at 85% 75%, rgba(63,111,196,.45) 0, rgba(63,111,196,0) 28%),
      radial-gradient(circle at 15% 40%, var(--pine-light) 0, rgba(95,143,106,0) 35%),
      linear-gradient(120deg, var(--pine-deep), var(--pine-mid) 55%, var(--pine-deep));
  }
  .event-text {
    position: absolute; left: 141px; top: 128px; width: 918px; height: 540px;
    text-align: center; color: var(--white);
  }
  .host {
    position: absolute; top: 96px; width: 100%;
    font: 700 26px/1 "Montserrat", sans-serif; letter-spacing: 1px;
  }
  .presents {
    position: absolute; top: 124px; left: 256px; width: 408px; height: 20px;
    display: flex; align-items: center; gap: 6px;
    font: italic 800 17px/1 "Montserrat", sans-serif; color: var(--rule-yellow);
  }
  .presents .rule { flex: 1; height: 2px; background: var(--rule-yellow); }
  .title-script {
    position: absolute; top: 150px; width: 100%;
    font: 400 82px/88px "Kaushan Script", cursive; color: var(--lime);
  }
  .title-sans {
    position: absolute; top: 328px; width: 100%;
    font: 400 82px/1 "Questrial", sans-serif; color: var(--red);
  }
  .divider {
    position: absolute; top: 404px; left: 189px; width: 560px; height: 2px;
    background: var(--rule-pale);
  }
  .date {
    position: absolute; top: 423px; width: 100%;
    font: 600 27px/1 "Montserrat", sans-serif; letter-spacing: 4px;
  }
</style>
</head>
<body>
<main class="canvas">
  <div class="hero-photo" role="img" aria-label="Close-up photo of evergreen fir branches with soft blue bokeh Christmas lights"></div>
  <section class="event-text">
    <p class="host">CEDAR HOLLOW BAPTIST CHURCH</p>
    <p class="presents"><span class="rule"></span>presents<span class="rule"></span></p>
    <h1 class="title-script">Marwood<br>Holiday</h1>
    <p class="title-sans">Jubilee 2025</p>
    <div class="divider"></div>
    <p class="date">DECEMBER 14 &amp; 15 6:00PM</p>
  </section>
</main>
</body>
</html>
```